I need a new business card design for my pharmacy.

I need a business card design. I will include my logo.
The card needs to be readable. I prefer to have my logo on one side along with my website, the other side includes the other information. Please use combination of black, neon green, white, and silver. This needs to catch the eye but yet be clearly visible and legible. Thanks

Industry/Entity Type

Pharmacy

Contact Information for Business Card

It needs to have the following information listed:
Mel's Apothecary Owner/Pharm D.
7134 North Brook Lane
Cedar Ridge, MN 55412
Phone 612-318-6207
Fax 612-318-6209
email: mel@melsapothecary-example.com
www.melsapothecary-example.com
Store hours Monday-Friday 9 am- 6 pm
Saturday 9 am- 1 pm
Sunday Closed
Please utilize the colors black, white, and neon green, maybe silver.

Requirements
Must have
• It needs to be easily readable!
Nice to have
• It should catch the eye.
Should not have
• Do not use any other colors except listed: black, neon green, white, & silver.

```html
<!DOCTYPE html>
<html lang="en">
<head>
<meta charset="utf-8">
<title>Mel's Apothecary — Business Card</title>
<link href="https://fonts.googleapis.com/css2?family=Open+Sans:wght@400;600;700&display=swap" rel="stylesheet">
<style>
  :root {
    --bg: #dcdcdc;
    --paper: #f4f4f2;
    --ink: #161616;
    --silver: #6d6e70;
    --neon: #8dc63f;
    --white: #ffffff;
  }
  * { box-sizing: border-box; margin: 0; padding: 0; }
  html, body { width: 1200px; height: 900px; overflow: hidden; }
  body {
    background: var(--bg);
    font-family: "Open Sans", Arial, sans-serif;
    position: relative;
  }
  .card {
    position: absolute;
    left: 285px;
    width: 630px;
    height: 360px;
    background: var(--paper);
    overflow: hidden;
    box-shadow: 0 6px 18px rgba(0,0,0,0.12);
  }
  .card--front { top: 75px; }
  .card--back { top: 465px; }

  .brand {
    position: absolute;
    display: flex;
    align-items: center;
    color: var(--ink);
    font-weight: 700;
    letter-spacing: -0.5px;
    white-space: nowrap;
  }
  .brand__dot {
    background: var(--neon);
    border-radius: 50%;
    margin-right: 14px;
    flex: none;
  }
  .card--front .brand { left: 60px; top: 72px; font-size: 44px; }
  .card--front .brand__dot { width: 26px; height: 26px; }

  .front-band {
    position: absolute;
    left: 0; right: 0; bottom: 0;
    height: 160px;
    background: var(--silver);
    border-top: 7px solid var(--neon);
  }
  .website {
    text-align: center;
    color: var(--white);
    font-size: 25px;
    letter-spacing: 3px;
    margin-top: 38px;
    white-space: nowrap;
  }
  .hours {
    text-align: center;
    color: var(--ink);
    font-size: 14px;
    margin-top: 28px;
    white-space: nowrap;
  }
  .hours__sep {
    display: inline-block;
    width: 6px; height: 6px;
    border-radius: 50%;
    background: var(--neon);
    margin: 0 6px 2px;
  }

  .card--back .brand { left: 40px; top: 22px; font-size: 22px; }
  .card--back .brand__dot { width: 14px; height: 14px; margin-right: 10px; }
  .back-panel {
    position: absolute;
    left: 0; top: 78px; right: 0; bottom: 0;
    background: var(--silver);
    border-top: 4px dotted var(--neon);
  }
  .back-stripe {
    position: absolute;
    top: 78px; right: 0; bottom: 0;
    width: 28px;
    background: var(--neon);
  }
  .contact {
    position: absolute;
    right: 62px;
    top: 128px;
    list-style: none;
    color: var(--white);
    font-size: 16px;
    text-align: right;
  }
  .contact__item {
    display: flex;
    justify-content: flex-end;
    align-items: center;
    gap: 12px;
    line-height: 1.35;
    white-space: nowrap;
  }
  .contact__item--address { margin-bottom: 20px; }
  .contact__icon { width: 16px; height: 16px; flex: none; }
</style>
</head>
<body>

  <section class="card card--front" aria-label="Card front">
    <div class="brand"><span class="brand__dot"></span>Mel's Apothecary</div>
    <div class="front-band">
      <p class="website">www.melsapothecary-example.com</p>
      <p class="hours">Monday-Friday 9 am- 6 pm<span class="hours__sep"></span>Saturday 9 am- 1 pm<span class="hours__sep"></span>Sunday Closed</p>
    </div>
  </section>

  <section class="card card--back" aria-label="Card back">
    <div class="brand"><span class="brand__dot"></span>Mel's Apothecary</div>
    <div class="back-panel"></div>
    <div class="back-stripe"></div>
    <ul class="contact">
      <li class="contact__item contact__item--address">
        <span>7134 North Brook Lane<br>Cedar Ridge, MN 55412</span>
        <svg class="contact__icon" viewBox="0 0 16 16"><path d="M8 1a5 5 0 0 0-5 5c0 4 5 9 5 9s5-5 5-9a5 5 0 0 0-5-5z" fill="none" stroke="#8dc63f" stroke-width="1.6"/><circle cx="8" cy="6" r="1.8" fill="#8dc63f"/></svg>
      </li>
      <li class="contact__item">
        <span>612-318-6207</span>
        <svg class="contact__icon" viewBox="0 0 16 16"><path d="M4 1.5l2 3-1.3 1.5a8 8 0 0 0 5.3 5.3L11.5 10l3 2-1 2.5C7.5 14.5 1.5 8.5 1.5 2.5z" fill="#8dc63f"/></svg>
      </li>
      <li class="contact__item">
        <span>612-318-6209</span>
        <svg class="contact__icon" viewBox="0 0 16 16"><rect x="4" y="1.5" width="8" height="4" fill="none" stroke="#8dc63f" stroke-width="1.4"/><rect x="1.5" y="5.5" width="13" height="6" fill="#8dc63f"/><rect x="4" y="10" width="8" height="4.5" fill="none" stroke="#8dc63f" stroke-width="1.4"/></svg>
      </li>
      <li class="contact__item">
        <span>mel@melsapothecary-example.com</span>
        <svg class="contact__icon" viewBox="0 0 16 16"><rect x="1.5" y="3.5" width="13" height="9" fill="none" stroke="#8dc63f" stroke-width="1.5"/><path d="M1.5 3.5L8 9l6.5-5.5" fill="none" stroke="#8dc63f" stroke-width="1.5"/></svg>
      </li>
    </ul>
  </section>

</body>
</html>
```